Bref créative
Wedding photographer business card
and stationary
Bright & Fun-filled
Lora Bexley
no address needed
lorabexley@mailvista.net
www.lorabexley.net
I like sleek but also fun and feminine.
corrected phone number given to winning designer for finalizing design.
Thanks
Special offer,
$50 off,
a package & a free 8x10 print
I have two designs so you may choose either logo to design.
here's the monogram for my second logo
the flowers for logo 2

```html
<!DOCTYPE html>
<html lang="en">
<head>
<meta charset="utf-8">
<title>Lora Bexley Photography — Stationery</title>
<link rel="stylesheet" href="https://fonts.googleapis.com/css2?family=Great+Vibes&family=Arimo:wght@400;700&display=swap">
<style>
  :root {
    --canvas: #efedeb;
    --paper: #ffffff;
    --pink: #e0456a;
    --pink-soft: #f3b9c6;
    --brown: #4a2f2c;
    --ink: #3a3a3a;
    --muted: #8a8a8a;
    --band: #ececec;
    --rule: #d8d8d8;
  }
  * { box-sizing: border-box; margin: 0; padding: 0; }
  html, body { width: 1200px; height: 1050px; overflow: hidden; }
  body {
    background: var(--canvas);
    font-family: "Arimo", Arial, sans-serif;
    color: var(--ink);
    position: relative;
  }
  .sheet {
    position: absolute;
    background: var(--paper);
    box-shadow: 0 2px 8px rgba(0,0,0,0.12);
    overflow: hidden;
  }
  .brand-name {
    font-family: "Great Vibes", cursive;
    color: var(--ink);
    font-weight: 400;
    line-height: 1;
  }
  .brand-tag {
    font-size: 9px;
    letter-spacing: 4px;
    color: var(--muted);
    text-transform: uppercase;
  }
  .floral {
    position: absolute;
    border-radius: 50%;
    background: radial-gradient(circle, rgba(224,69,106,0.55) 0%, rgba(243,185,198,0.35) 55%, rgba(255,255,255,0) 75%);
  }

  /* Business card front */
  .card-front { left: 40px; top: 40px; width: 480px; height: 270px; }
  .card-front .logo { position: absolute; top: 50px; left: 0; right: 0; text-align: center; }
  .card-front .brand-name { font-size: 52px; }
  .card-front .floral { width: 70px; height: 60px; top: 34px; left: 300px; }
  .card-front .contact { position: absolute; top: 148px; left: 0; right: 0; text-align: center; font-size: 11px; line-height: 17px; color: var(--muted); }
  .card-front .contact .email { color: var(--pink); }
  .card-bar { position: absolute; left: 0; right: 0; bottom: 14px; height: 26px; background: var(--brown); color: #fff; font-size: 11px; text-align: center; line-height: 26px; letter-spacing: 0.5px; }
  .card-bar + .card-line { position: absolute; left: 0; right: 0; bottom: 0; height: 14px; background: var(--pink-soft); }

  /* Business card back */
  .card-back { left: 40px; top: 340px; width: 480px; height: 270px; }
  .card-back .floral { width: 150px; height: 130px; top: -10px; left: -20px; }
  .card-back .offer-title { position: absolute; top: 52px; left: 0; right: 0; text-align: center; font-family: "Great Vibes", cursive; font-size: 50px; color: var(--ink); }
  .card-back .offer-badge { position: absolute; top: 118px; left: 210px; width: 60px; height: 60px; border-radius: 50%; background: var(--brown); color: #fff; font-size: 11px; text-align: center; line-height: 14px; padding-top: 16px; }
  .card-back .offer-text { position: absolute; top: 192px; left: 0; right: 0; text-align: center; font-size: 15px; letter-spacing: 1.5px; color: var(--pink); }

  /* Envelope */
  .envelope { left: 40px; top: 650px; width: 500px; height: 300px; }
  .envelope .address { position: absolute; top: 40px; left: 110px; width: 300px; }
  .envelope .address-label { font-size: 12px; color: var(--ink); letter-spacing: 1px; margin-bottom: 6px; }
  .envelope .address-line { height: 30px; border-bottom: 1px solid var(--rule); }
  .envelope .band { position: absolute; left: 0; right: 0; bottom: 0; height: 46px; background: linear-gradient(90deg, #ffffff 0%, var(--pink-soft) 40%, var(--pink) 100%); }
  .envelope .logo { position: absolute; left: 34px; bottom: 62px; }
  .envelope .brand-name { font-size: 40px; }
  .envelope .floral { width: 120px; height: 90px; left: 20px; bottom: 70px; }

  /* Letterhead */
  .letterhead { left: 580px; top: 40px; width: 580px; height: 960px; }
  .letterhead .header { height: 92px; background: var(--band); border-bottom: 3px solid var(--pink); text-align: center; padding-top: 20px; }
  .letterhead .brand-name { font-size: 40px; }
  .letterhead .header .floral { width: 60px; height: 50px; top: 10px; left: 320px; }
  .letterhead .meta { position: absolute; top: 112px; left: 36px; right: 36px; font-size: 11px; line-height: 20px; }
  .letterhead .letter-no { position: absolute; top: 0; right: 0; font-size: 10px; color: var(--muted); }
  .letterhead .meta b { font-weight: 700; }
  .letterhead .recipient { margin-top: 6px; line-height: 15px; }
  .letterhead .meta-rule { margin-top: 14px; border-bottom: 1px solid var(--rule); }
  .letterhead .sign-off { position: absolute; left: 36px; bottom: 90px; font-size: 11px; line-height: 17px; }
  .letterhead .floral-corner { position: absolute; right: 20px; bottom: 80px; width: 150px; height: 120px; background: radial-gradient(circle, rgba(224,69,106,0.18) 0%, rgba(243,185,198,0.12) 50%, rgba(255,255,255,0) 75%); }
  .letterhead .footer { position: absolute; left: 0; right: 0; bottom: 0; height: 54px; background: linear-gradient(90deg, var(--brown) 0%, #6d3a42 55%, var(--pink) 100%); color: #fff; font-size: 11px; display: flex; justify-content: center; align-items: center; gap: 22px; }
</style>
</head>
<body>

<section class="sheet card-front">
  <div class="floral" role="img" aria-label="Floral ornament beside the logo"></div>
  <div class="logo">
    <div class="brand-name">Lora Bexley</div>
    <div class="brand-tag">Photography</div>
  </div>
  <div class="contact">
    <div>555-014-2273</div>
    <div class="email">lorabexley@mailvista.net</div>
  </div>
  <div class="card-bar">www.lorabexley.net</div><div class="card-line"></div>
</section>

<section class="sheet card-back">
  <div class="floral" role="img" aria-label="Cluster of roses ornament"></div>
  <div class="offer-title">Special Offer</div>
  <div class="offer-badge">$50<br>off</div>
  <div class="offer-text">a package &amp; a free 8x10 print</div>
  <div class="card-bar">www.lorabexley.net</div><div class="card-line"></div>
</section>

<section class="sheet envelope">
  <div class="address">
    <div class="address-label">TO</div>
    <div class="address-line"></div>
    <div class="address-line"></div>
    <div class="address-line"></div>
    <div class="address-line"></div>
  </div>
  <div class="floral" role="img" aria-label="Cluster of roses ornament behind the logo"></div>
  <div class="logo">
    <div class="brand-name">Lora Bexley</div>
    <div class="brand-tag">Photography</div>
  </div>
  <div class="band"></div>
</section>

<section class="sheet letterhead">
  <header class="header">
    <div class="floral" role="img" aria-label="Floral ornament beside the logo"></div>
    <div class="brand-name">Lora Bexley</div>
    <div class="brand-tag">Photography</div>
  </header>
  <div class="meta">
    <div class="letter-no">Letter No: 1000456</div>
    <div><b>Date:</b> DD/MM/YY</div>
    <div><b>Subject:</b> Subject Title of the Letter Here</div>
    <div><b>To:</b></div>
    <div class="recipient">Mr. Customer Name<br>Company Name</div>
    <div class="meta-rule"></div>
  </div>
  <div class="floral-corner" role="img" aria-label="Faint floral ornament"></div>
  <div class="sign-off">Thanking you,<br>Lora Bexley</div>
  <footer class="footer">
    <span>Email: lorabexley@mailvista.net</span>
    <span>-</span>
    <span>Website: www.lorabexley.net</span>
    <span>-</span>
    <span>Phone: 555-014-2273</span>
  </footer>
</section>

</body>
</html>
```